Bright Oak Consultant Services

I'm looking to create a flyer for my business to provide a consultant service. I will be providing the following below
Launch Your Business Today for only $150
(state fee not included)
Business Formation includes:
*Limited liability Corporation (LLC)
*Hale and Penwick Number
*FEIN
*Operation Agreement for partnership LLCs (For 2 or more member(s)
*Commercial Activity license (If needed for your Business )
*Same -day turnaround service with documents
Schedule your Appointment today
Call or text:413-902-6175
Email:MorvellCapitalCircle@quillpost.net
Target Market(s)
I want the flyer to attract people who wants to start a business but doesn’t know where to start. I want the flyer to stand out form the other consultant businesses.
Industry/Entity Type
Consultant
Requirements
Must have
- The State fee not included should be in small print
Highlight the price or service
Highlight the phrase "launch you business today"
Nice to have
- Different samples of colors, a variety
Should not have
- should not be all one color

```html
<!DOCTYPE html>
<html lang="en">
<head>
<meta charset="utf-8">
<title>Bright Oak Consultant Services – Launch Your Business Today</title>
<link rel="stylesheet" href="https://fonts.googleapis.com/css2?family=Montserrat:wght@500;600;700;800&family=Catamaran:wght@500;600&display=swap">
<style>
  :root {
    --stage: #e8e5e0;
    --ink-dark: #11141d;
    --paper: #ffffff;
    --orange: #f07622;
    --coral: #ec4f55;
    --red-orange: #ea4228;
    --text: #111111;
    --white: #ffffff;
  }
  * { margin: 0; padding: 0; box-sizing: border-box; }
  html, body {
    width: 1200px; height: 800px; overflow: hidden;
    background: var(--stage);
  }
  .flyer {
    position: absolute; left: 305px; top: 20px;
    width: 590px; height: 760px;
    background: var(--paper);
    box-shadow: 0 6px 24px rgba(0,0,0,0.18);
    overflow: hidden;
    font-family: "Catamaran", sans-serif;
    color: var(--text);
  }
  .hero {
    position: absolute; left: 0; top: 0; width: 100%; height: 276px;
    background: var(--ink-dark);
    text-align: center;
    font-family: "Montserrat", sans-serif;
  }
  .hero-line { position: absolute; left: 0; width: 100%; line-height: 1; }
  .hero-launch { top: 22px; font-size: 61px; font-weight: 600; color: var(--white); letter-spacing: 0.5px; }
  .hero-business { top: 86px; font-size: 84px; font-weight: 800; color: var(--white); letter-spacing: -1px; }
  .hero-today { top: 170px; font-size: 61px; font-weight: 600; color: var(--orange); }
  .accent-band {
    position: absolute; left: 0; top: 276px; width: 100%; height: 61px;
    background: linear-gradient(90deg, var(--orange) 0%, var(--orange) 55%, var(--coral) 68%, var(--coral) 100%);
  }
  .price {
    position: absolute; left: 0; top: 452px; width: 280px; text-align: center;
    font-family: "Montserrat", sans-serif;
  }
  .price-lead { font-size: 48px; font-weight: 500; line-height: 1; letter-spacing: -0.5px; }
  .price-amount { margin-top: 12px; font-size: 54px; font-weight: 800; line-height: 1; }
  .price-note { margin-top: 8px; font-family: "Catamaran", sans-serif; font-size: 11px; font-weight: 500; }
  .services { position: absolute; left: 303px; top: 382px; width: 280px; }
  .services-title {
    font-family: "Montserrat", sans-serif; font-size: 14px; font-weight: 700;
    letter-spacing: -0.2px; margin-bottom: 11px;
  }
  .services-list { list-style: none; }
  .services-list li {
    position: relative; padding-left: 16px;
    font-size: 14.5px; font-weight: 500; line-height: 17.5px;
    margin-bottom: 10px;
  }
  .services-list li::before {
    content: ""; position: absolute; left: 0; top: 5px;
    width: 8px; height: 8px; border-radius: 50%; background: var(--text);
  }
  .cta {
    position: absolute; left: 0; top: 657px; width: 100%; padding-left: 0;
    text-align: center; font-family: "Montserrat", sans-serif;
    font-size: 12.5px; font-weight: 700; text-indent: -30px;
  }
  .contact-band {
    position: absolute; left: 0; bottom: 0; width: 100%; height: 80px;
    background: linear-gradient(90deg, var(--red-orange) 0%, var(--orange) 100%);
    color: var(--white);
  }
  .community {
    position: absolute; left: 12px; top: 24px;
    font-family: "Montserrat", sans-serif; font-size: 12.5px; font-weight: 500; line-height: 16px;
  }
  .contact-row {
    position: absolute; left: 266px; display: flex; align-items: center; gap: 8px;
    font-family: "Montserrat", sans-serif; font-weight: 500;
  }
  .contact-phone { top: 12px; font-size: 14.5px; }
  .contact-email { top: 46px; font-size: 12.5px; }
  .contact-note { font-family: "Catamaran", sans-serif; font-size: 12px; }
  .contact-icon { width: 22px; height: 22px; flex: none; }
</style>
</head>
<body>
  <main class="flyer">
    <header class="hero">
      <p class="hero-line hero-launch">Launch Your</p>
      <h1 class="hero-line hero-business">BUSINESS</h1>
      <p class="hero-line hero-today">Today</p>
    </header>
    <div class="accent-band"></div>

    <section class="price">
      <p class="price-lead">FOR ONLY</p>
      <p class="price-amount">$150</p>
      <p class="price-note">(state fee not included)</p>
    </section>

    <section class="services">
      <h2 class="services-title">BUSINESS FORMATION INCLUDES:</h2>
      <ul class="services-list">
        <li>Limited liability Corporation (LLC)</li>
        <li>Hale and Penwick Number</li>
        <li>FEIN</li>
        <li>Operation Agreement for partnership<br>LLCs (For 2 or more member(s)</li>
        <li>Commercial Activity license<br>(If needed for your Business )</li>
        <li>Same -day turnaround service<br>with documents</li>
      </ul>
    </section>

    <p class="cta">SCHEDULE YOUR APPOINTMENT TODAY</p>

    <footer class="contact-band">
      <p class="community">To Join With<br>Our Community</p>
      <p class="contact-row contact-phone">
        <svg class="contact-icon" viewBox="0 0 24 24" aria-hidden="true">
          <path fill="#ffffff" d="M6.6 2.5c.6-.4 1.4-.3 1.8.3l2.3 3.4c.4.6.3 1.3-.2 1.8l-1.5 1.3c.9 2 2.6 3.9 4.6 5l1.4-1.4c.5-.5 1.3-.6 1.9-.2l3.3 2.4c.6.4.7 1.2.3 1.8l-1.3 2c-.6.9-1.7 1.3-2.7 1C9.6 18 5.4 13.6 3.4 7.3c-.3-1 .1-2.1 1-2.7z"/>
        </svg>
        <span>413-902-6175</span> <span class="contact-note">(Call or text)</span>
      </p>
      <p class="contact-row contact-email">
        <svg class="contact-icon" viewBox="0 0 24 24" aria-hidden="true">
          <rect x="2" y="5" width="20" height="14" fill="none" stroke="#ffffff" stroke-width="1.6"/>
          <path d="M2 5l10 8 10-8M2 19l7.5-7M22 19l-7.5-7" fill="none" stroke="#ffffff" stroke-width="1.6"/>
        </svg>
        <span>MorvellCapitalCircle@quillpost.net</span>
      </p>
    </footer>
  </main>
</body>
</html>
```